Design of machine exterior and promotion wall

Overview: The task includes the design of the Pennyvault promotional stand, compromising the exterior of the Pennyvault machine as well as the promotional wall that will be placed directly behind it.

Deliverable: Coherently designed, well layered and high resolution PSD / EPS files with appropriate bleed margin for the front of the promotion wall, the back of the promotion wall and the machine exterior. Preview picture of branded machine in front of branded wall.

Details can be found in the attached design brief.

```html
<!DOCTYPE html>
<html lang="en">
<head>
<meta charset="utf-8">
<title>Pennyvault promotion wall</title>
<link rel="stylesheet" href="https://fonts.googleapis.com/css2?family=Open+Sans:wght@600;700&display=swap">
<style>
  :root {
    --gold: #c8974a;
    --gold-deep: #b9853a;
    --gold-text: #d3a24f;
    --brand-brown: #a7824c;
    --paper: #f4f4f4;
    --paper-shade: #dcdcdc;
    --white: #ffffff;
    --panel-grey: rgba(175, 175, 175, 0.55);
  }
  html, body {
    margin: 0;
    padding: 0;
    overflow: hidden;
    background: var(--white);
  }
  .wall {
    position: relative;
    width: 1200px;
    height: 827px;
    overflow: hidden;
    background: linear-gradient(160deg, var(--white) 0%, var(--paper) 45%, var(--paper-shade) 100%);
    font-family: "Open Sans", Arial, sans-serif;
  }
  .wall-swoosh {
    position: absolute;
    inset: 0;
    width: 1200px;
    height: 827px;
  }
  .headline {
    position: absolute;
    left: 0;
    width: 980px;
    margin: 0;
    text-align: center;
    color: var(--gold-text);
    font-weight: 700;
    font-size: 38px;
    line-height: 53px;
  }
  .headline--warning { top: 64px; }
  .headline--offer { top: 226px; }
  .store-mark {
    position: absolute;
    left: 252px;
    top: 346px;
    width: 74px;
    display: flex;
    flex-direction: column;
    align-items: center;
    gap: 3px;
    color: var(--gold-text);
    font-weight: 700;
    font-size: 13px;
    line-height: 16px;
  }
  .store-mark__dot {
    width: 56px;
    height: 56px;
    border-radius: 50%;
    background: var(--gold-text);
  }
  .store-line {
    position: absolute;
    top: 355px;
    left: 336px;
    margin: 0;
    color: var(--gold-text);
    font-weight: 700;
    font-size: 38px;
    line-height: 53px;
    white-space: nowrap;
  }
  .brand {
    position: absolute;
    left: 795px;
    top: 314px;
    display: flex;
    align-items: center;
    gap: 8px;
    color: var(--brand-brown);
    font-weight: 600;
    font-size: 26px;
  }
  .brand__square {
    width: 14px;
    height: 14px;
    background: var(--brand-brown);
  }
  .machine-panel {
    position: absolute;
    left: 775px;
    width: 203px;
    background: var(--panel-grey);
  }
  .machine-panel--top { top: 394px; height: 121px; }
  .machine-panel--mid { top: 522px; height: 137px; }
  .machine-panel--base { top: 668px; height: 159px; }
  .free-badge {
    position: absolute;
    left: 398px;
    top: 476px;
    width: 118px;
    height: 118px;
  }
  .steps {
    position: absolute;
    left: 182px;
    top: 606px;
    display: flex;
    gap: 12px;
  }
  .step {
    position: relative;
    width: 184px;
    height: 150px;
  }
  .step__number {
    position: absolute;
    left: 2px;
    top: 14px;
    width: 30px;
    height: 30px;
    border-radius: 50%;
    background: var(--white);
    color: var(--gold);
    font-weight: 700;
    font-size: 20px;
    line-height: 30px;
    text-align: center;
    z-index: 1;
  }
  .step__scene {
    position: absolute;
    left: 40px;
    top: 0;
    width: 144px;
    height: 150px;
    border-radius: 6px;
    background: linear-gradient(180deg, rgba(255,255,255,0.32), rgba(255,255,255,0.18));
  }
</style>
</head>
<body>
<main class="wall">
  <svg class="wall-swoosh" viewBox="0 0 1200 827" aria-hidden="true">
    <path d="M0 300 C 350 330, 800 200, 1200 110 L1200 140 C 800 240, 380 360, 0 340 Z" fill="#e6e6e6"/>
    <path d="M0 520 C 400 560, 800 420, 1200 240 L1200 827 L0 827 Z" fill="var(--gold)"/>
    <path d="M0 520 C 400 560, 800 420, 1200 240 L1200 270 C 820 450, 420 585, 0 560 Z" fill="var(--gold-deep)" opacity="0.55"/>
    <path d="M0 540 C 420 600, 820 440, 1200 230" fill="none" stroke="var(--white)" stroke-width="10" opacity="0.95"/>
    <path d="M0 510 C 400 540, 780 400, 1200 210" fill="none" stroke="var(--white)" stroke-width="3" opacity="0.7"/>
  </svg>

  <h1 class="headline headline--warning">Don't get stuck with coins<br>you can't spend!</h1>
  <h2 class="headline headline--offer">Turn your change into a voucher<br>to be redeemed at any</h2>

  <div class="store-mark"><span class="store-mark__dot"></span>Travelmart</div>
  <p class="store-line">store in this airport.</p>

  <div class="brand"><span class="brand__square"></span>Pennyvault</div>

  <div class="machine-panel machine-panel--top"></div>
  <div class="machine-panel machine-panel--mid"></div>
  <div class="machine-panel machine-panel--base"></div>

  <svg class="free-badge" viewBox="0 0 124 124" role="img" aria-label="100% Free Service">
    <polygon fill="var(--white)" stroke="var(--gold)" stroke-width="2"
      points="62,2 70,14 83,6 87,21 102,17 101,32 116,34 109,47 122,55 111,64 120,76 106,81 110,96 95,96 93,111 79,106 72,120 62,110 52,120 45,106 31,111 29,96 14,96 18,81 4,76 13,64 2,55 15,47 8,34 23,32 22,17 37,21 41,6 54,14"/>
    <g transform="rotate(18 62 62)" fill="var(--gold)" font-family="Open Sans, Arial, sans-serif" font-weight="700" text-anchor="middle">
      <text x="62" y="56" font-size="24">100%</text>
      <text x="62" y="76" font-size="14">Free</text>
      <text x="62" y="92" font-size="14">Service</text>
    </g>
  </svg>

  <section class="steps">
    <div class="step">
      <span class="step__number">1</span>
      <div class="step__scene" role="img" aria-label="Traveller with suitcase holding leftover coins, thinking of destination currencies"></div>
    </div>
    <div class="step">
      <span class="step__number">2</span>
      <div class="step__scene" role="img" aria-label="Traveller dropping coins into the free machine and receiving a voucher"></div>
    </div>
    <div class="step">
      <span class="step__number">3</span>
      <div class="step__scene" role="img" aria-label="Traveller paying with card and voucher at the store counter"></div>
    </div>
  </section>
</main>
</body>
</html>
```